Harlow Auto , a Dealership and Repair Shop in Marengo Iowa

Harlow Auto is a repair shop and auto sales dealership that offers oil changes, alignments, tires, air conditioning work, computer diagnostics. Focused on Vantras, Marlo and Brisk. Small business with less than 10 employees. Billboard sign is in town and not the larger billboard
billboard is 8ft x 18ft

Target Market(s)

General public

Industry/Entity Type

automotive

Font styles to use
Serif
Sans Serif

Colors

Designer to choose colors to be used in the design.

Requirements
Must have
• Located 3 miles west of Alderton. Sales and service. Phone number 319-555-0187
Nice to have
• Picture of a car or truck, or both. picture of wrench
Should not have
• Not sure

```html
<!DOCTYPE html>
<html lang="en">
<head>
<meta charset="utf-8">
<title>Harlow Auto — Sales and Service</title>
<link rel="stylesheet" href="https://fonts.googleapis.com/css2?family=Anton&family=Oswald:wght@600;700&display=swap">
<style>
  :root {
    --cream: #f8f2e0;
    --red: #d93c3e;
    --navy: #13283d;
  }
  html, body {
    margin: 0;
    padding: 0;
    width: 1200px;
    height: 1200px;
    overflow: hidden;
    background: var(--navy);
  }
  .billboard {
    display: block;
    width: 1200px;
    height: 1200px;
  }
  .panel-cream { fill: var(--cream); }
  .panel-red { fill: var(--red); }
  .panel-navy { fill: var(--navy); }
  .brand-name {
    font-family: "Anton", "Oswald", sans-serif;
    fill: var(--navy);
  }
  .brand-sub {
    font-family: "Anton", "Oswald", sans-serif;
    fill: var(--red);
  }
  .info-line {
    font-family: "Oswald", "Roboto Condensed", sans-serif;
    font-weight: 700;
    fill: var(--cream);
  }
  .phone {
    font-family: "Anton", "Oswald", sans-serif;
    fill: var(--red);
  }
  .truck-art { fill: var(--cream); opacity: 0.9; }
  .wrench-art { fill: var(--cream); opacity: 0.85; }
</style>
</head>
<body>
<svg class="billboard" viewBox="0 0 1200 1200" xmlns="http://www.w3.org/2000/svg">
  <rect class="panel-cream" x="0" y="0" width="724" height="616"/>
  <rect class="panel-red" x="724" y="0" width="476" height="616"/>
  <rect class="panel-navy" x="0" y="616" width="1200" height="584"/>

  <text class="brand-name" x="96" y="316" font-size="275" textLength="1008" lengthAdjust="spacingAndGlyphs">HARLOW</text>
  <text class="brand-sub" x="92" y="556" font-size="237" textLength="576" lengthAdjust="spacingAndGlyphs">AUTO</text>

  <rect class="truck-art" role="img" aria-label="Illustration of a white pickup truck in front three-quarter view" x="708" y="376" width="492" height="240" rx="24"/>
  <rect class="wrench-art" role="img" aria-label="Illustration of a large cream open-end wrench" x="916" y="656" width="284" height="276" rx="24"/>

  <text class="info-line" x="92" y="732" font-size="63" textLength="736" lengthAdjust="spacingAndGlyphs">LOCATED 3 MILES WEST</text>
  <text class="info-line" x="92" y="812" font-size="63" textLength="430" lengthAdjust="spacingAndGlyphs">OF ALDERTON</text>
  <text class="info-line" x="92" y="920" font-size="87" textLength="808" lengthAdjust="spacingAndGlyphs">SALES AND SERVICE</text>

  <text class="phone" x="80" y="1116" font-size="177" textLength="1044" lengthAdjust="spacingAndGlyphs">319-555-0187</text>
</svg>
</body>
</html>
```